Website Design for a New Business Sharing Application

Purpose: Website for a new product – a sharing application called "Gathr.io"

Product concept: Easy sharing of business information. The application has different sections: tasks, calendars, documents, contacts, notes and links. The key feature of the application is that you can drag and drop information from different sections into a "share." A share is a page which lists all the types of information that you drag into it. You can add people to this "share."

Note: The application itself is not part of this project, just the website.

Website details: The site, in addition to being informational, will actually be the first point of entry for visitors into the application itself. Because of that, we would like the website design to reflect the look of the application, to create a smooth and seamless experience for the user moving from the website into the application (tough the website does not need to look *exactly* like the application). Included Product Tour screenshots show you the look of the application.

Website pages to be created: 4 pages
We are flexible in terms of the exact structure and placement of elements. You may change that any way you like. The pages are as follows:

Home page
Product Tour page
Press page
Blog page

Specific description of pages are provided in project files we will upload. We will also upload the logo, home page layout we have in mind, and other supporting files.

NOTE: Please submit first the design of the home page. Based on this design we will ask selected designers to submit designs for the other pages.

Target Market(s)

Business people who want to share work related files with their colleagues

Industry/Entity Type

Business

Requirements
Must have
• All the required features are listed in the description of the website and specific pages that we will upload.

```html
<!DOCTYPE html>
<html lang="en">
<head>
<meta charset="utf-8">
<title>Gathr.io – Share Now</title>
<link href="https://fonts.googleapis.com/css2?family=Open+Sans:wght@300;400;600;700&family=Ubuntu:wght@500&display=swap" rel="stylesheet">
<style>
:root{
  --bg:#ffffff;
  --text:#555a5e;
  --muted:#8a8f93;
  --blue:#2a7fc4;
  --blue-dark:#1d5fa8;
  --orange:#ee7a2f;
  --band:#ebebeb;
  --footer:#2e2e2e;
  --footer-text:#d6d6d6;
  --line:#e3e3e3;
  --app-dark:#2b2e33;
}
*{box-sizing:border-box;margin:0;padding:0}
html,body{width:1200px;height:1141px;overflow:hidden;background:var(--bg);font-family:"Open Sans",Arial,sans-serif;color:var(--text)}
.page{position:relative;width:1200px;height:1141px}
.stripe{position:absolute;top:0;left:0;width:100%;height:2px;background:linear-gradient(90deg,#2a7fc4 0 20%,#d9d9d9 20% 31%,#ee7a2f 31% 45%,#6bbf4e 45% 58%,#e44b4b 58% 70%,#f2b632 70% 84%,#9b6cc9 84%)}
.brand{position:absolute;left:141px;top:40px;display:flex;align-items:center;gap:10px}
.brand-dot{width:40px;height:40px;border-radius:50%;background:var(--orange)}
.brand-name{font-family:"Ubuntu",sans-serif;font-weight:500;font-size:32px;color:var(--blue)}
.social-counter{position:absolute;top:55px;display:flex;gap:4px;font-size:11px}
.social-counter .btn{border:1px solid #b9c4d6;background:#eef1f6;padding:1px 5px;color:#34558b;font-weight:600}
.social-counter .count{border:1px solid #c9c9c9;padding:1px 4px;color:#333}
.access{position:absolute;left:891px;top:41px;width:158px;height:42px;border-radius:22px;background:#e6e6e6;padding:4px}
.access span{display:block;height:34px;border-radius:18px;background:linear-gradient(#f38a3e,#e26a1f);color:#fff;font-size:13px;line-height:34px;text-align:center}
.hero-title{position:absolute;top:140px;width:100%;text-align:center;font-weight:300;font-size:60px;color:#6d7276}
.hero-title b{font-family:"Ubuntu",sans-serif;font-weight:500;color:var(--blue);border-bottom:3px dashed var(--blue);padding-bottom:0;line-height:1}
.hero-sub{position:absolute;top:222px;width:100%;text-align:center;font-size:28px;color:#5c6166}
.hero-sub strong{font-weight:600;color:#4a4e52}
.rule{position:absolute;left:216px;width:750px;height:1px;background:var(--line);box-shadow:0 2px 4px rgba(0,0,0,.05)}
.features{position:absolute;left:0;top:318px;width:100%;display:flex;justify-content:center;gap:25px}
.feature{display:flex;flex-direction:column;align-items:center;gap:12px;font-size:19px;font-weight:300;color:#70757a}
.feature svg{width:32px;height:32px}
.dropzone{position:absolute;left:214px;top:488px;width:247px;height:70px;border:1px dashed #9a9a9a;display:flex;align-items:center;gap:14px;padding-left:12px;font-size:12.5px;color:#555}
.dropzone .plus{font-size:38px;font-weight:300;color:#aaa;line-height:1}
.or-also{position:absolute;left:520px;top:503px;font-size:20px;font-weight:300;color:#777}
.signup{position:absolute;left:741px;top:502px;width:243px;height:44px;border-radius:3px;background:linear-gradient(#3a87d6,var(--blue-dark));border:1px solid #1a4f8c;color:#fff;font-weight:600;font-size:15px;line-height:42px;padding-left:25px}
.signup i{font-style:normal;margin-left:12px;font-weight:700}
.screen{position:absolute;background:#f4f4f4;box-shadow:0 0 14px rgba(0,0,0,.25);overflow:hidden}
.screen .bar{height:24px;background:var(--app-dark);display:flex;align-items:center;padding-left:10px;gap:6px}
.screen .bar .b-dot{width:8px;height:8px;border-radius:50%;background:var(--orange)}
.screen .bar .b-name{color:#fff;font-size:8px;font-weight:600}
.screen .body{position:absolute;top:24px;left:0;right:0;bottom:0}
.screen-left{left:150px;top:666px;width:250px;height:269px}
.screen-left .body{background:linear-gradient(160deg,#e9e4dc 0,#f3f3f3 40%,#e7eef5 100%)}
.screen-right{left:765px;top:666px;width:285px;height:269px}
.screen-right .body{background:linear-gradient(180deg,#eef0f2 0,#f7f7f7 30%,#eef5ea 100%)}
.screen-main{left:392px;top:619px;width:379px;height:316px;z-index:2}
.screen-main .side{position:absolute;left:0;top:24px;width:72px;bottom:0;background:#f0f0f0;border-right:1px solid #ddd}
.screen-main .cover{position:absolute;left:73px;top:24px;right:0;height:105px;background:linear-gradient(120deg,#e2b43a,#c9475c 35%,#3e8fc9 65%,#6cb24a)}
.screen-main .cards{position:absolute;left:73px;top:129px;right:0;bottom:0;background:linear-gradient(180deg,#f9f9f9,#eeeeee)}
.band{position:absolute;left:0;top:935px;width:100%;height:148px;background:var(--band)}
.video{position:absolute;left:215px;top:959px;width:160px;height:100px;border:1px solid #a8a8a8;background:#cfcfcf;padding:8px}
.video div{width:100%;height:100%;background:linear-gradient(160deg,#22324a,#0d121b)}
.band-title{position:absolute;font-weight:300;font-size:30px;color:#5a5f63}
.band-note{position:absolute;left:411px;top:1019px;font-size:14px;color:#666}
.tour-arrow{position:absolute;left:923px;top:978px}
.footer{position:absolute;left:0;top:1083px;width:100%;height:58px;background:var(--footer)}
.footer-nav a{position:absolute;top:21px;font-size:11.5px;color:var(--footer-text);text-decoration:none}
.social-dot{position:absolute;top:14px;width:30px;height:30px;border-radius:50%;background:#e6e6e6}
</style>
</head>
<body>
<div class="page">
  <div class="stripe"></div>

  <header>
    <div class="brand"><span class="brand-dot"></span><span class="brand-name">Gathr.io</span></div>
    <div class="social-counter" style="left:639px"><span class="btn">Like</span><span class="count">2.4k</span></div>
    <div class="social-counter" style="left:731px"><span class="btn">Follow</span><span class="count">1,527 followers</span></div>
    <a class="access"><span>Access your shares&nbsp; ››</span></a>
  </header>

  <h1 class="hero-title">Share <b>NOW</b></h1>
  <p class="hero-sub">Drag information, add People, <strong>BOOM!</strong></p>

  <div class="rule" style="top:287px"></div>
  <ul class="features">
    <li class="feature"><svg viewBox="0 0 32 32"><rect x="9" y="4" width="17" height="22" fill="#8fc17a"/><rect x="5" y="8" width="17" height="22" fill="#5aa84a"/><path d="M9 14h9M9 18h9M9 22h9" stroke="#fff" stroke-width="2"/></svg>Files</li>
    <li class="feature"><svg viewBox="0 0 32 32"><rect x="2" y="5" width="28" height="22" fill="#cfe8f7" stroke="#58aedc" stroke-width="2"/><path d="M4 25l8-9 6 6 4-4 6 7z" fill="#58aedc"/><circle cx="22" cy="11" r="3" fill="#58aedc"/></svg>Photos</li>
    <li class="feature"><svg viewBox="0 0 32 32"><rect x="3" y="9" width="26" height="18" rx="2" fill="#e4453d"/><rect x="11" y="5" width="10" height="5" fill="none" stroke="#e4453d" stroke-width="2"/><path d="M3 17h26" stroke="#fff" stroke-width="1.5"/></svg>Tasks</li>
    <li class="feature"><svg viewBox="0 0 32 32"><path d="M8 3h16v26l-8-7-8 7z" fill="#8f5bc8"/></svg>To-dos</li>
    <li class="feature"><svg viewBox="0 0 32 32"><rect x="3" y="6" width="26" height="23" fill="#3b3f44"/><rect x="6" y="12" width="20" height="14" fill="#fff"/><path d="M9 3v6M23 3v6" stroke="#3b3f44" stroke-width="3"/><path d="M8 15h16M8 19h16M8 23h16" stroke="#3b3f44" stroke-width="1.5" stroke-dasharray="2 2"/></svg>Calendars</li>
    <li class="feature"><svg viewBox="0 0 32 32"><path d="M6 26l2-6 16-16 4 4-16 16z" fill="#f2b632"/><path d="M6 26l2-6 4 4z" fill="#7a6030"/></svg>Notes</li>
    <li class="feature"><svg viewBox="0 0 32 32"><g fill="none" stroke="#e4453d" stroke-width="3"><rect x="3" y="15" width="14" height="8" rx="4" transform="rotate(-30 10 19)"/><rect x="15" y="9" width="14" height="8" rx="4" transform="rotate(-30 22 13)"/></g></svg>Links</li>
  </ul>
  <div class="rule" style="top:427px"></div>

  <div class="dropzone"><span class="plus">+</span>Drag files here to share imediately</div>
  <p class="or-also">Or you can also ...</p>
  <a class="signup">Sign Up Now, Its FREE !! <i>›</i></a>

  <section class="screens">
    <div class="screen screen-left" role="img" aria-label="App view listing shares as photo cards">
      <div class="bar"><span class="b-dot"></span><span class="b-name">Gathr.io</span></div>
      <div class="body"></div>
    </div>
    <div class="screen screen-right" role="img" aria-label="App view of task cards with due dates">
      <div class="bar"></div>
      <div class="body"></div>
    </div>
    <div class="screen screen-main" role="img" aria-label="App view of a single share with cover photo and content cards">
      <div class="bar"><span class="b-dot"></span><span class="b-name">Gathr.io</span></div>
      <div class="side"></div>
      <div class="cover"></div>
      <div class="cards"></div>
    </div>
  </section>

  <section class="band">
  </section>
  <div class="video" role="img" aria-label="Video still of a stage performance"><div></div></div>
  <h2 class="band-title" style="left:408px;top:977px">What is it?</h2>
  <p class="band-note">Watch the video</p>
  <h2 class="band-title" style="left:741px;top:989px">Take the tour</h2>
  <svg class="tour-arrow" width="62" height="56" viewBox="0 0 62 56"><path d="M4 54C6 30 20 20 40 20V6l20 20-20 20V32C24 32 12 38 4 54z" fill="#a9acaf"/></svg>

  <footer class="footer">
    <nav class="footer-nav">
      <a style="left:150px">Home</a>
      <a style="left:212px">About Us</a>
      <a style="left:285px">Product Tour</a>
      <a style="left:380px">Pricing</a>
      <a style="left:442px">Terms of Use</a>
      <a style="left:534px">Jobs</a>
      <a style="left:587px">Sign-Up</a>
      <a style="left:654px">Blog</a>
      <a style="left:705px">Press</a>
      <a style="left:760px">Contact Us</a>
    </nav>
    <span class="social-dot" style="left:941px"></span>
    <span class="social-dot" style="left:981px"></span>
    <span class="social-dot" style="left:1020px"></span>
  </footer>
</div>
</body>
</html>
```